Tilda Tinkerwire, An IT Company Has New Logo, Need Fresh Business Cards

IT company is called Tilda Tinkerwire and is displayed nicely with the new logo from here on pitchloft. Would like a fresh business card look that encompasses the idea that we want clients to Cherish Every Gadget. I love the use of circuitry with hearts as endpoints and x's and o's. It needs to have room for my certification logos of which there are 4 and a BRJ Alumni log. I am attaching my current card to illustrate how it has always captured attention, but that was in the early stages of business when I was doing more residential work. I am focused on businesses now, so a level of professionalism is necessary. I would also like the card to lend itself well to additional stationary, email signature, ticketing template for my workboard, etc. For the time being, I need the card for an upcoming conference so that work will come later. Color scheme should be that of the new logo. Thank you and I look forward to the designs.

Target Market(s)

Businesses looking for IT services.

Industry/Entity Type

Information Technology

Contact Information for Business Card

See above

Requirements
Must have
• New logo colors and a warm feel. Possibly a tad feminine as I am female, but appealing to males.
Nice to have
• I would like techy, but no too much so. I like friendly and connecting feels. People LOVED my old card and called me because it gave them a warm feeling.

```html
<!DOCTYPE html>
<html lang="en">
<head>
<meta charset="utf-8">
<title>Tilda Tinkerwire – Business Cards</title>
<link rel="stylesheet" href="https://fonts.googleapis.com/css2?family=Varela+Round&family=Roboto+Condensed:wght@700&display=swap">
<style>
  :root {
    --backdrop: #2b2a27;
    --card: #ffffff;
    --pink: #f2a6c8;
    --blue: #8fd0ee;
    --green: #c6dd84;
    --name: #6cbfe6;
    --tagline: #e48cb4;
    --band-text: #ffffff;
  }
  * { box-sizing: border-box; margin: 0; padding: 0; }
  html, body {
    width: 1200px;
    height: 857px;
    overflow: hidden;
    background: var(--backdrop);
  }
  .canvas {
    position: relative;
    width: 1200px;
    height: 857px;
  }
  .card {
    position: absolute;
    background: var(--card);
    border-radius: 26px;
    overflow: hidden;
  }
  .brand {
    display: flex;
    flex-direction: column;
    align-items: center;
    justify-content: center;
  }
  .brand-mark {
    width: 84px;
    height: 84px;
    border-radius: 50%;
    background: linear-gradient(135deg, var(--pink), var(--blue) 55%, var(--green));
    margin-bottom: 14px;
  }
  .brand-name {
    font-family: "Varela Round", sans-serif;
    color: var(--name);
    font-size: 36px;
    letter-spacing: -0.5px;
    white-space: nowrap;
    line-height: 1.1;
  }
  .brand-tagline {
    font-family: "Varela Round", sans-serif;
    color: var(--tagline);
    font-size: 11px;
    letter-spacing: 3.2px;
    text-transform: uppercase;
    margin-top: 6px;
    white-space: nowrap;
  }

  /* Front: logo only */
  .card--front {
    left: 90px;
    top: 278px;
    width: 525px;
    height: 300px;
    display: flex;
    align-items: center;
    justify-content: center;
  }

  /* Back: logo, contact bands, certification space */
  .card--back {
    left: 720px;
    top: 166px;
    width: 300px;
    height: 525px;
    display: flex;
    flex-direction: column;
  }
  .card--back .brand { height: 196px; }
  .card--back .brand-mark { width: 62px; height: 62px; margin-bottom: 10px; }
  .card--back .brand-name { font-size: 28px; }
  .card--back .brand-tagline { font-size: 9px; letter-spacing: 2.4px; }

  .contact-band {
    height: 78px;
    margin-bottom: 10px;
    display: flex;
    align-items: center;
    justify-content: center;
    font-family: "Roboto Condensed", sans-serif;
    font-weight: 700;
    color: var(--band-text);
    white-space: nowrap;
    clip-path: polygon(0 10%, 100% 0, 100% 90%, 0 100%);
  }
  .contact-band--phone { background: var(--pink); font-size: 38px; letter-spacing: 0.5px; }
  .contact-band--web   { background: var(--blue); font-size: 19px; }
  .contact-band--email { background: var(--green); font-size: 17px; height: 86px; }

  .certification-space {
    flex: 1;
  }
</style>
</head>
<body>
  <main class="canvas">
    <section class="card card--front" aria-label="Card front">
      <div class="brand">
        <div class="brand-mark" role="img" aria-label="Logo mark"></div>
        <p class="brand-name">Tilda Tinkerwire</p>
        <p class="brand-tagline">Cherish Every Gadget</p>
      </div>
    </section>

    <section class="card card--back" aria-label="Card back">
      <div class="brand">
        <div class="brand-mark" role="img" aria-label="Logo mark"></div>
        <p class="brand-name">Tilda Tinkerwire</p>
        <p class="brand-tagline">Cherish Every Gadget</p>
      </div>
      <p class="contact-band contact-band--phone">407-555-0182</p>
      <p class="contact-band contact-band--web">www.tilda-tinkerwire.com</p>
      <p class="contact-band contact-band--email">tilda.tinkerwire@mailpost.com</p>
      <div class="certification-space" aria-label="Space reserved for certification badges"></div>
    </section>
  </main>
</body>
</html>
```